Estate Agent/Real Estate valuation tool

We need a design for our our new estate agent valuation tool.

The tool allows users to book a valuation of their house/property with the estate agent, after they choose there property they can then complete their details and choose a booking time.

The mock up of the design we want is attached to this project.(Main Screen)

This also needs to be responsive so the design is easy to use on a mobile device.

Target Market(s)

estate agents

Industry/Entity Type

Real Estate Agent

Number of Pages Required

1 page

Requirements
Must have
• Section 2 and 3 greyed out when user is on step 1
• Section 1 and 3 greyed out when user is on step 2
• Section 1 and 2 greyed out when the user is on step 3
• *** Design must be shown for mobile/ipad and desktop
Nice to have
• Clean and Simple
Should not have
• Dark colours

```html
<!DOCTYPE html>
<html lang="en">
<head>
<meta charset="utf-8">
<meta name="viewport" content="width=device-width, initial-scale=1">
<title>Harbourline Estates – Book a Valuation</title>
<link href="https://fonts.googleapis.com/css2?family=Noto+Serif:wght@400;600;700&display=swap" rel="stylesheet">
<style>
  :root {
    --brand-blue: #3596da;
    --rule-dark: #333333;
    --stage-grey: #b0b0b0;
    --panel-active: #d6d6d6;
    --panel-muted: #c8c8c8;
    --field-active: #f2f2f2;
    --field-muted: #e4e4e4;
    --bar-grey: #666666;
    --text-dark: #111111;
    --text-muted: #4a4a4a;
    --error-red: #ee1111;
    --tab-border: #888888;
    --active-top: #b0dcfa;
    --active-bottom: #2c8dd5;
    --muted-top: #ffffff;
    --muted-bottom: #858585;
  }
  * { box-sizing: border-box; margin: 0; padding: 0; }
  html, body { width: 100%; }
  body {
    font-family: "Noto Serif", Georgia, serif;
    background: var(--brand-blue);
    color: var(--text-dark);
    display: flex; flex-direction: column; min-height: 100vh;
  }

  /* Header */
  .site-header {
    height: 187px; background: var(--brand-blue);
    display: flex; align-items: center; justify-content: center; gap: 14px;
  }
  .brand-mark { width: 34px; height: 34px; border-radius: 50%; background: #ffffff; }
  .brand-name { font-size: 34px; font-weight: 700; color: #ffffff; }
  .header-rule { height: 9px; background: var(--rule-dark); }

  /* Booking stage */
  .booking-stage {
    background: var(--stage-grey);
    padding: 29px 20px 62px;
    display: flex; justify-content: center; gap: 20px;
  }
  .site-footer { flex: 1; min-height: 221px; background: var(--brand-blue); }

  /* Step panels */
  .step {
    width: 300px; height: 393px;
    display: flex; flex-direction: column;
    background: var(--panel-muted);
  }
  .step--current { background: var(--panel-active); }
  .step-title {
    height: 56px; flex: none;
    display: flex; align-items: center; justify-content: center;
    font-size: 15px; font-weight: 700; color: var(--text-muted);
    background: linear-gradient(var(--muted-top), var(--muted-bottom));
  }
  .step--current .step-title {
    color: #ffffff;
    background: linear-gradient(var(--active-top), var(--active-bottom));
  }
  .step-body { flex: 1; display: flex; flex-direction: column; }
  .step-status {
    height: 65px; flex: none;
    border-top: 9px solid var(--bar-grey);
    display: flex; align-items: center; justify-content: center;
    font-size: 22px; font-weight: 600; color: var(--text-muted);
  }
  .step-status--confirm {
    background: linear-gradient(var(--muted-top), var(--muted-bottom));
  }

  /* Form parts */
  .field-label { display: block; font-size: 15px; line-height: 22px; }
  .field { display: block; height: 32px; background: var(--field-muted); }
  .step--current .field { background: var(--field-active); }

  .step--property .step-body { padding: 0 18px 0 19px; }
  .step--property .field-label { margin-top: 2px; padding-left: 7px; }
  .postcode-row { display: flex; margin-top: 2px; }
  .postcode-row .field { flex: 1; }
  .search-button {
    width: 80px; height: 32px;
    display: flex; align-items: center; justify-content: center;
    font-size: 15px; font-weight: 700; color: #ffffff;
    background: linear-gradient(var(--active-top), var(--active-bottom));
  }
  .error-note {
    margin-top: 4px; height: 28px;
    border: 3px dashed var(--error-red); color: var(--error-red);
    font-size: 15px; display: flex; align-items: center; justify-content: center;
  }
  .address-field { margin-top: 14px; }
  .address-field:first-of-type { margin-top: 15px; }

  .step--details .step-body { padding: 0 20px 0 17px; }
  .label-name { margin-top: 1px; padding-left: 1px; }
  .field-name { margin-top: 3px; }
  .label-email { margin-top: 8px; padding-left: 4px; }
  .field-email { margin-top: 7px; }
  .label-phone { margin-top: 10px; padding-left: 4px; }
  .field-phone { margin-top: 5px; }

  .step--time .step-body { padding: 0 21px 0 17px; }
  .day-tabs { display: flex; height: 37px; margin-top: 17px; }
  .day-tab {
    flex: 1; display: flex; align-items: center; justify-content: center;
    background: var(--panel-muted); border: 1px solid var(--tab-border);
    font-size: 8px; letter-spacing: -0.3px; white-space: nowrap; overflow: hidden;
  }
  .day-tab--today { font-size: 11px; letter-spacing: 0; }
  .slot-list { display: flex; flex-direction: column; gap: 4px; margin-top: 4px; }
  .slot-row { display: flex; gap: 10px; }
  .slot-time { flex: 1; height: 32px; background: var(--field-muted); }
  .slot-pick { width: 47px; height: 32px; background: var(--field-muted); }

  /* Desktop canvas */
  @media (min-width: 1025px) {
    html, body { height: 901px; overflow: hidden; }
  }

  /* Tablet */
  @media (max-width: 1024px) {
    .booking-stage { flex-wrap: wrap; }
    .step { width: calc(50% - 10px); max-width: 360px; }
  }

  /* Mobile */
  @media (max-width: 640px) {
    .site-header { height: 110px; }
    .brand-name { font-size: 24px; }
    .booking-stage { flex-direction: column; align-items: stretch; padding: 20px 14px 40px; }
    .step { width: 100%; max-width: none; height: auto; }
    .step-body { padding-bottom: 20px !important; }
    .day-tab { font-size: 9px; }
  }
</style>
</head>
<body>
  <header class="site-header">
    <span class="brand-mark"></span>
    <span class="brand-name">Harbourline Estates</span>
  </header>
  <div class="header-rule"></div>

  <main class="booking-stage">
    <section class="step step--property step--current">
      <h2 class="step-title">STEP 1 of 3 - Property details</h2>
      <div class="step-body">
        <span class="field-label">Postcode</span>
        <div class="postcode-row">
          <span class="field"></span>
          <span class="search-button">Search</span>
        </div>
        <div class="error-note">Error: Postcode invalid</div>
        <span class="field address-field"></span>
        <span class="field address-field"></span>
        <span class="field address-field"></span>
      </div>
      <div class="step-status">UNFINISHED</div>
    </section>

    <section class="step step--details">
      <h2 class="step-title">STEP 2 of 3 - Your details</h2>
      <div class="step-body">
        <span class="field-label label-name">Your name</span>
        <span class="field field-name"></span>
        <span class="field-label label-email">Your email</span>
        <span class="field field-email"></span>
        <span class="field-label label-phone">Your contact number</span>
        <span class="field field-phone"></span>
      </div>
      <div class="step-status">UNFINISHED</div>
    </section>

    <section class="step step--time">
      <h2 class="step-title">STEP 3 of 3 - Appointment time</h2>
      <div class="step-body">
        <div class="day-tabs">
          <span class="day-tab day-tab--today">today</span>
          <span class="day-tab">tomorrow</span>
          <span class="day-tab">Mon 30th</span>
          <span class="day-tab">Tue 1st</span>
          <span class="day-tab">Wed 2nd</span>
          <span class="day-tab">Thurs 3rd</span>
          <span class="day-tab">Fri 4th</span>
        </div>
        <div class="slot-list">
          <div class="slot-row"><span class="slot-time"></span><span class="slot-pick"></span></div>
          <div class="slot-row"><span class="slot-time"></span><span class="slot-pick"></span></div>
          <div class="slot-row"><span class="slot-time"></span><span class="slot-pick"></span></div>
          <div class="slot-row"><span class="slot-time"></span><span class="slot-pick"></span></div>
          <div class="slot-row"><span class="slot-time"></span><span class="slot-pick"></span></div>
        </div>
      </div>
      <div class="step-status step-status--confirm">CONFIRM BOOKING</div>
    </section>
  </main>

  <footer class="site-footer"></footer>
</body>
</html>
```